The Pixel Tap Business card.

A Simple card with our Logo and contact information. To give to investors and other professionals.

We are a nerd themed bar.
our target market is young professionals age 21+ but the real purpose of this business card is to present to potential investors and other professionals with our contact information. as we are still looking for funding before we start up.

I am partial to green and my partner likes red we are open to iteration.

Target Market(s)

Investors

Industry/Entity Type

Business

Contact Information for Business Card

Martin Hale (225) 730-6192 kent.h4711@mailnest.test Glen Porter (225) 968-5037 glenp318@mailnest.test

Font styles to use
Serif

Requirements
Nice to have
• Keep it simple but not boring.
• Use the Logos but feel free to edit them to match theme/colors.
• Keep the back clean and use one of the Logos.

```html
<!DOCTYPE html>
<html lang="en">
<head>
<meta charset="utf-8">
<title>The Pixel Tap – Business Card</title>
<link href="https://fonts.googleapis.com/css2?family=PT+Sans:wght@400;700&display=swap" rel="stylesheet">
<style>
  :root {
    --ink: #0a0a0a;
    --paper: #ffffff;
    --accent-green: #2fc22b;
    --text-light: #f2f2f2;
    --stage: #e6e4e1;
    --card-w: 860px;
    --card-h: 492px;
  }
  * { box-sizing: border-box; margin: 0; padding: 0; }
  html, body {
    width: 1200px;
    height: 1120px;
    overflow: hidden;
    background: var(--stage);
    font-family: "PT Sans", Arial, sans-serif;
  }
  .card {
    position: absolute;
    left: 170px;
    width: var(--card-w);
    height: var(--card-h);
    overflow: hidden;
    box-shadow: 0 8px 24px rgba(0,0,0,.18);
  }
  .card--front {
    top: 46px;
    background: var(--paper);
    border: 40px solid var(--ink);
    display: flex;
    align-items: center;
    justify-content: center;
  }
  .card--back { top: 584px; background: var(--paper); display: flex; }

  /* front */
  .front-logo-box {
    width: 560px;
    height: 176px;
    border: 2px solid var(--ink);
    display: flex;
    align-items: center;
    justify-content: center;
  }
  .brand-name {
    font-family: "PT Sans", Arial, sans-serif;
    font-weight: 700;
    color: var(--ink);
    text-transform: uppercase;
    letter-spacing: 1px;
    line-height: 1;
    white-space: nowrap;
  }
  .front-logo-box .brand-name { font-size: 64px; }

  /* back */
  .back-brand {
    width: 52%;
    display: flex;
    align-items: center;
    justify-content: center;
    border-right: 4px solid var(--accent-green);
  }
  .back-brand .brand-name { font-size: 54px; }
  .back-contacts {
    flex: 1;
    background: var(--ink);
    padding: 98px 0 0 56px;
  }
  .contact { margin-bottom: 42px; }
  .contact__name {
    color: var(--accent-green);
    font-weight: 700;
    font-size: 25px;
    text-transform: uppercase;
    margin-bottom: 12px;
  }
  .contact__line {
    display: flex;
    align-items: center;
    gap: 10px;
    color: var(--text-light);
    font-size: 20px;
    margin-bottom: 5px;
  }
  .contact__icon { width: 16px; height: 16px; flex: none; }
</style>
</head>
<body>

<section class="card card--front" aria-label="Card front">
  <div class="front-logo-box">
    <span class="brand-name">The Pixel Tap</span>
  </div>
</section>

<section class="card card--back" aria-label="Card back">
  <div class="back-brand">
    <span class="brand-name">The Pixel Tap</span>
  </div>
  <div class="back-contacts">
    <div class="contact">
      <p class="contact__name">Martin Hale</p>
      <p class="contact__line">
        <svg class="contact__icon" viewBox="0 0 16 16"><circle cx="8" cy="8" r="7" fill="none" stroke="#2fc22b" stroke-width="1.6"/><path d="M5.5 4.5l1.5 0 .6 2-1 .8a5 5 0 0 0 2.1 2.1l.8-1 2 .6 0 1.5c-3.5.4-6.4-2.5-6-6z" fill="#2fc22b"/></svg>
        (225) 730-6192
      </p>
      <p class="contact__line">
        <svg class="contact__icon" viewBox="0 0 16 16"><rect x="1" y="4" width="14" height="9" rx="1" fill="#2fc22b"/><path d="M1.5 4.5L8 9l6.5-4.5" fill="none" stroke="#0a0a0a" stroke-width="1.2"/></svg>
        kent.h4711@mailnest.test
      </p>
    </div>
    <div class="contact">
      <p class="contact__name">Glen Porter</p>
      <p class="contact__line">
        <svg class="contact__icon" viewBox="0 0 16 16"><circle cx="8" cy="8" r="7" fill="none" stroke="#2fc22b" stroke-width="1.6"/><path d="M5.5 4.5l1.5 0 .6 2-1 .8a5 5 0 0 0 2.1 2.1l.8-1 2 .6 0 1.5c-3.5.4-6.4-2.5-6-6z" fill="#2fc22b"/></svg>
        (225) 968-5037
      </p>
      <p class="contact__line">
        <svg class="contact__icon" viewBox="0 0 16 16"><rect x="1" y="4" width="14" height="9" rx="1" fill="#2fc22b"/><path d="M1.5 4.5L8 9l6.5-4.5" fill="none" stroke="#0a0a0a" stroke-width="1.2"/></svg>
        glenp318@mailnest.test
      </p>
    </div>
  </div>
</section>

</body>
</html>
```